Make a dull looking powerpoint look very sharp

Dear Gigmaven,

Please take a look at the sales powerpoint that I have shared with you.
The powerpoint is 11 pages long.

I would like you to make the powerpoint look stunning using simple graphics to make the powerpoint look great and appealing to customers. We will send the powerpoint to our leads to explain to them what it is we can offer to them.

The text in the powerpoint is correct. So use the text that is provided on the powerpoint page.

I challenge you to come up with unique design that look professional and stunning for the eye.

If you have any question, please let me know.

I would like to see a total design, not only one page.

```html
<!DOCTYPE html>
<html lang="en">
<head>
<meta charset="utf-8">
<title>VentureAtlas – Partner Deck</title>
<link href="https://fonts.googleapis.com/css2?family=Roboto:wght@300;400;500;700&display=swap" rel="stylesheet">
<style>
:root{
  --stage:#1c1c1d;
  --brand:#0a4a9c;
  --brand-deep:#083f86;
  --ink-blue:#0b3a8c;
  --accent:#4aa3ff;
  --slate:#3a3b3e;
  --paper:#ffffff;
  --ink:#1d1d1f;
  --muted:#555a60;
}
*{margin:0;padding:0;box-sizing:border-box}
html,body{width:693px;height:1200px;overflow:hidden;background:var(--stage)}
body{font-family:"Roboto",Arial,sans-serif;color:var(--ink)}
.deck{position:relative;width:815px;height:1412px;transform:scale(0.85);transform-origin:0 0}
.slide{position:absolute;width:402px;height:226px;overflow:hidden;background:var(--paper)}
.slide > *,.side > *,.band > *,.list > li,.list > li > .mark{position:absolute}
.col-left{left:0}.col-right{left:413px}
.dark{background:var(--slate);color:#fff}
.blue{background:var(--brand);color:#fff}
.side{top:0;height:226px}
.h1{font-weight:700;font-size:24px;color:var(--ink);letter-spacing:-.2px}
.lead{font-weight:700;color:var(--ink-blue);font-size:10.5px;line-height:1.25}
.body{font-size:8.5px;line-height:1.35;color:var(--muted)}
.rule{height:2px;background:var(--accent)}
.list{list-style:none}
.link{color:var(--ink-blue);font-weight:700;text-decoration:underline}
</style>
</head>
<body>
<main class="deck">

  <section class="slide blue col-left" style="top:0">
    <div role="img" aria-label="Faint world map backdrop" style="inset:0;background:radial-gradient(ellipse at 70% 30%,#1a5bb0 0%,var(--brand) 55%,var(--brand-deep) 100%)"></div>
    <h1 style="left:72px;top:68px;font-size:26px;font-weight:500;color:#fff">VentureAtlas.co</h1>
    <div class="rule" style="left:72px;top:105px;width:72px"></div>
    <p style="left:75px;top:126px;font-size:15px;font-weight:300;color:#fff;line-height:1.35;width:165px">Your voice to reach the Founder community</p>
  </section>

  <section class="slide dark col-right" style="top:0;background:#3d3d3f">
    <h2 style="left:32px;top:16px;font-size:24px;font-weight:500;color:#fff">Trend</h2>
    <p style="left:32px;top:52px;font-size:10px;font-weight:300;color:#ddd;line-height:1.25;width:172px">9 out of 10 Companies are struggling to connect with startups</p>
    <div role="img" aria-label="Sketch of hands holding an innovation doodle sheet" style="left:34px;top:130px;width:80px;height:54px;border-radius:2px;background:linear-gradient(#f3f3f3,#dcdcdc)"></div>
    <p style="left:139px;top:155px;font-size:11px;font-weight:300;color:#eee;line-height:1.2;width:105px">What if the startups came to you?</p>
    <div class="side blue" style="left:252px;width:150px">
      <h3 style="left:23px;top:16px;font-size:15px;font-weight:500">Venture Atlas</h3>
      <p style="left:23px;top:47px;font-size:10.5px;font-weight:500;line-height:1.25;width:100px">Helps you to reach startup founders to</p>
      <ul class="list" style="left:23px;top:96px;font-size:8.5px;font-weight:300;width:120px">
        <li style="top:0">•&nbsp;&nbsp; Make announcements</li>
        <li style="top:22px">•&nbsp;&nbsp; Sell your services</li>
        <li style="top:49px">•&nbsp;&nbsp; Spread your events</li>
      </ul>
      <div style="left:23px;top:182px;width:110px;height:1px;background:#fff"></div>
      <p style="left:23px;top:191px;font-size:8px;font-weight:300;line-height:1.25;width:115px">We are inviting you to join our partner program</p>
    </div>
  </section>

  <section class="slide col-left" style="top:236px">
    <h2 class="h1" style="left:60px;top:50px">Trend</h2>
    <p class="lead" style="left:60px;top:88px;width:180px">We’re only really at the stage where people are learning to walk</p>
    <p class="body" style="left:60px;top:140px;width:182px">“Large corporates are realizing they need to engage on a formal basis and have someone at the organization whose job or part of their job is to engage with emerging tech and startups”</p>
    <div class="side dark" style="left:305px;width:97px">
      <div role="img" aria-label="Portrait photo of Noah Lindqvist" style="left:20px;top:50px;width:56px;height:56px;border-radius:50%;background:radial-gradient(circle,#f07c5c 0%,#d9452e 100%)"></div>
      <p style="left:0;top:121px;width:97px;text-align:center;font-size:8.5px;font-weight:500">Noah Lindqvist</p>
      <p style="left:13px;top:165px;width:82px;font-size:5.5px;font-weight:300;line-height:1.5;color:#ddd">Founder and lead of the Northgate Startup Challenge in London</p>
    </div>
  </section>

  <section class="slide col-right" style="top:236px">
    <h2 class="h1" style="left:45px;top:62px">Opportunity</h2>
    <p class="lead" style="left:45px;top:101px;width:170px">Be a driving force on the platform that startup founders love</p>
    <p style="left:45px;top:146px;width:185px;font-size:8.5px;line-height:1.35;color:var(--ink)">People naturally trust parties that support the communities they are a part of.</p>
    <div class="side dark" style="left:264px;width:138px">
      <p style="left:20px;top:83px;width:105px;font-size:10.5px;font-weight:300;line-height:1.2">What if we could help you to build that trust and help you spread your companies voice at the same time?</p>
    </div>
  </section>

  <section class="slide col-left" style="top:474px">
    <h2 class="h1" style="left:67px;top:8px">Solution</h2>
    <div style="left:0;top:42px;width:402px;height:2px;background:var(--brand)"></div>
    <p class="lead" style="left:68px;top:83px;width:270px;font-size:9.5px">Venture Atlas is an online tool to find venture funding that is supported by companies that want to reach startups</p>
    <p class="body" style="left:68px;top:126px;width:122px;color:var(--ink)">We help companies to reach this highly targeted audience by sponsoring website real-estate</p>
    <p class="body" style="left:212px;top:126px;width:125px;color:var(--ink)">We help startup to find venture funding for free based on stage, industry and country</p>
    <div class="band" style="left:0;top:200px;width:402px;height:26px;background:var(--brand)">
      <p style="left:67px;top:8px;font-size:10px;font-weight:700;color:var(--accent)">In Short</p>
      <p style="left:221px;top:5px;font-size:6.5px;color:#fff;line-height:1.35;width:125px">By supporting Venture Atlas you support your local startup community</p>
    </div>
  </section>

  <section class="slide col-right" style="top:474px">
    <h2 class="h1" style="left:28px;top:38px">Why now?</h2>
    <p class="lead" style="left:28px;top:74px;width:130px">Traditional strategies to reach startups fall short</p>
    <p style="left:28px;top:110px;font-size:9px;color:var(--ink)">Efforts limited by:</p>
    <p class="body" style="left:28px;top:158px;font-size:7.5px">The lack of trust startups have in corporates</p>
    <p class="body" style="left:28px;top:174px;width:160px;font-size:7.5px">A lack of value that you bring when spreading your message</p>
    <div class="side blue" style="left:224px;width:178px">
      <p style="left:13px;top:55px;width:160px;font-size:10.5px;font-weight:700;line-height:1.25">Become a Venture Atlas Partner and unlock the ability to:</p>
      <ul class="list" style="left:13px;top:98px;width:155px;font-size:7.5px;font-weight:300;line-height:1.35">
        <li style="top:0;padding-left:13px"><span class="mark" style="left:0;top:0">✓</span>Increase trust startup founders have in your brand</li>
        <li style="top:26px;padding-left:13px"><span class="mark" style="left:0;top:0">✓</span>Increase your overall brand awareness with in the startup community</li>
        <li style="top:52px;padding-left:13px"><span class="mark" style="left:0;top:0">✓</span>Spread your message to startups on a steady and predictable basis</li>
      </ul>
    </div>
  </section>

  <section class="slide dark col-left" style="top:712px">
    <h2 style="left:44px;top:30px;font-size:19px;font-weight:700">How does it work?</h2>
    <p style="left:44px;top:66px;width:155px;font-size:7px;line-height:1.4"><b>Startups visit Venture Atlas</b> to find investors per country</p>
    <p style="left:44px;top:100px;width:150px;font-size:7px;line-height:1.4">On the country page <b>they see that you’re a country partner</b></p>
    <p style="left:44px;top:137px;width:150px;font-size:7px;line-height:1.4"><b>Startups get massive value</b> from the free database “you” provide</p>
    <p style="left:44px;top:172px;width:150px;font-size:7px;line-height:1.4"><b>Provide targeted call2actions</b> and get startup leads on the country and investor pages</p>
    <div role="img" aria-label="Screenshot of the Netherlands country page sponsored by Bluepeak" style="left:258px;top:17px;width:102px;height:190px;background:linear-gradient(#ffffff 0,#ffffff 10%,#2f7fd8 10%,#1f63b8 30%,#2a2d33 30%,#2a2d33 94%,#1f63b8 94%)"></div>
  </section>

  <section class="slide dark col-right" style="top:712px">
    <ul class="list" style="left:42px;top:26px;width:150px;font-size:10px;font-weight:300;line-height:1.25">
      <li style="top:0;padding-left:25px;width:120px"><svg class="mark" style="left:0;top:3px" width="8" height="10" viewBox="0 0 8 10"><path d="M1 1l5 4-5 4" fill="none" stroke="#fff" stroke-width="1.8"/></svg>Reach your startup audience</li>
      <li style="top:39px;padding-left:25px;width:120px"><svg class="mark" style="left:0;top:3px" width="8" height="10" viewBox="0 0 8 10"><path d="M1 1l5 4-5 4" fill="none" stroke="#fff" stroke-width="1.8"/></svg>Support the startup ecosystem</li>
      <li style="top:77px;padding-left:25px;width:120px"><svg class="mark" style="left:0;top:3px" width="8" height="10" viewBox="0 0 8 10"><path d="M1 1l5 4-5 4" fill="none" stroke="#fff" stroke-width="1.8"/></svg>Spread your personal message</li>
      <li style="top:115px;padding-left:25px;width:120px"><svg class="mark" style="left:0;top:3px" width="8" height="10" viewBox="0 0 8 10"><path d="M1 1l5 4-5 4" fill="none" stroke="#fff" stroke-width="1.8"/></svg>Use your custom call2actions</li>
      <li style="top:152px;padding-left:25px;width:130px"><svg class="mark" style="left:0;top:3px" width="8" height="10" viewBox="0 0 8 10"><path d="M1 1l5 4-5 4" fill="none" stroke="#fff" stroke-width="1.8"/></svg>Bring value to your startup audience</li>
    </ul>
    <div role="img" aria-label="Screenshot of the Netherlands country page sponsored by Orbitcloud" style="left:242px;top:28px;width:118px;height:168px;background:linear-gradient(#ffffff 0,#ffffff 8%,#f07e1a 8%,#f07e1a 22%,#2a2d33 22%,#2a2d33 82%,#f07e1a 82%)"></div>
  </section>

  <section class="slide dark col-left" style="top:949px">
    <h2 style="left:0;top:78px;width:402px;text-align:center;font-size:26px;font-weight:700">For Live - Demo</h2>
    <a style="left:126px;top:128px;width:150px;height:38px;border:1px solid #9a9ca0;border-radius:7px;color:#fff;text-decoration:none;font-size:13px;line-height:36px;text-align:center">Click here</a>
  </section>

  <section class="slide col-right" style="top:949px">
    <h2 style="left:25px;top:28px;font-size:16px;font-weight:500;color:var(--ink)">I want to become a partner</h2>
    <p class="lead" style="left:25px;top:55px">Follow three simple steps</p>
    <span style="left:25px;top:96px;font-size:15px;color:var(--ink-blue);font-weight:500">01</span>
    <p class="body" style="left:64px;top:98px;width:130px;font-size:6.5px">Go to <span class="link">this link</span> and pick the countries you want to sponsor</p>
    <span style="left:25px;top:138px;font-size:15px;color:var(--ink-blue);font-weight:500">02</span>
    <p class="body" style="left:64px;top:132px;width:158px;font-size:6.5px">At the bottom of the page tell us which countries you would like to support and we will send you the price list for those countries</p>
    <span style="left:25px;top:179px;font-size:15px;color:var(--ink-blue);font-weight:500">03</span>
    <p class="body" style="left:64px;top:178px;width:162px;font-size:6.5px">We agree on the partnership and we go into the proces of incorporating your branding and your call2actions into the countries you choose to support</p>
    <div class="side blue" style="left:252px;width:150px">
      <h3 style="left:31px;top:8px;font-size:11px;font-weight:700">FAQ</h3>
      <ul class="list" style="left:31px;top:30px;width:88px;font-size:6.5px;font-weight:300;line-height:1.3">
        <li style="top:0">What is VentureAtlas.co?</li>
        <li style="top:17px">Why was VentureAtlas.co built?</li>
        <li style="top:42px">Why should I support Venture Atlas?</li>
        <li style="top:67px">What is the mission of Venture Atlas</li>
        <li style="top:92px">How can I use Venture Atlas to reach startups?</li>
        <li style="top:117px">Why do startups love Venture Atlas?</li>
        <li style="top:142px">When will it go live?</li>
        <li style="top:159px;text-decoration:underline">How do you differ from Dealgraph, SeedRoster and fundmap.io?</li>
      </ul>
    </div>
  </section>

  <section class="slide blue" style="left:207px;top:1187px;width:401px;height:225px">
    <h2 style="left:52px;top:70px;font-size:32px;font-weight:500">VentureAtlas</h2>
    <div style="left:52px;top:116px;width:92px;height:1px;background:#fff"></div>
    <p style="left:52px;top:139px;font-size:12.5px;font-weight:300">Support startups by bringing them true value</p>
  </section>

</main>
</body>
</html>
```